Kestwick Holdings AG needs web design

We need a website for a Swiss company: Kestwick Holdings AG. We offer our customers financial services such as advice and funds. We also have an interest rate calculator that we want to link to via a button on the website.

We are looking for a black and gold design. (Background: Black, Accents: Gold and White)
The design should convey security and growth. We have uploaded our logo in the attachment.
Font from the logo: Trajan Pro Regular

```html
<!DOCTYPE html>
<html lang="en">
<head>
<meta charset="utf-8">
<title>Kestwick Holdings AG</title>
<link href="https://fonts.googleapis.com/css2?family=Cinzel:wght@400;500;600&family=Montserrat:wght@400;500;600;700&display=swap" rel="stylesheet">
<style>
:root{
  --black:#000000;
  --ink:#0b0b0b;
  --panel:#151515;
  --gold:#c9ab72;
  --gold-light:#e3cc98;
  --gold-dark:#8f7645;
  --white:#ffffff;
  --muted:#d8d8d8;
  --line:#6e6e6e;
}
*{box-sizing:border-box;margin:0;padding:0}
html,body{width:1200px;height:5051px;overflow:hidden;background:var(--black)}
body{font-family:'Montserrat',Arial,sans-serif;color:var(--white);position:relative}
.serif{font-family:'Cinzel',Georgia,serif}
.abs{position:absolute}
.btn-gold{position:absolute;display:flex;align-items:center;justify-content:center;background:linear-gradient(180deg,var(--gold-light),var(--gold) 55%,#a98a54);color:var(--white);font-size:13px;font-weight:600;letter-spacing:.5px;text-transform:uppercase;border-radius:2px}
.btn-outline{position:absolute;display:flex;align-items:center;justify-content:center;border:1.5px solid var(--gold);color:var(--gold);font-size:13px;font-weight:600;text-transform:uppercase;border-radius:2px}

/* hero */
.hero{position:absolute;left:0;top:0;width:1200px;height:673px;overflow:hidden}
.hero-photo{position:absolute;inset:0;background:radial-gradient(ellipse 320px 380px at 680px 330px,#4a4a52 0%,#2a2a30 45%,transparent 75%),linear-gradient(90deg,#151516 0%,#2b2d31 45%,#3a3b40 70%,#1c1d20 100%)}
.hero-shade{position:absolute;inset:0;background:linear-gradient(90deg,rgba(0,0,0,.55) 0%,rgba(0,0,0,.1) 50%,rgba(0,0,0,.3) 100%)}
.brand{position:absolute;left:98px;top:40px;width:210px;text-align:center;font-family:'Cinzel',Georgia,serif;color:var(--gold);font-size:21px;line-height:26px}
.nav{position:absolute;top:40px;left:0;width:1200px;height:24px;font-size:15px}
.nav a{position:absolute;color:var(--white);text-decoration:none}
.nav a.active{color:var(--gold-light);border-bottom:2px solid var(--gold);padding-bottom:4px}
.hero-title{position:absolute;left:100px;top:236px;font-family:'Cinzel',Georgia,serif;font-size:60px;line-height:60px;color:var(--white)}
.hero-sub{position:absolute;left:100px;top:378px;width:400px;font-size:16px;line-height:29px}
.slide-arrow{position:absolute;top:320px}
.scroll-dot{position:absolute;left:578px;top:641px;width:44px;height:44px;border-radius:50%;background:var(--white);border:3px solid var(--gold)}

/* about */
.about-frame{position:absolute;left:100px;top:771px;width:210px;height:216px;background:var(--gold)}
.about-photo{position:absolute;left:122px;top:790px;width:456px;height:420px;background:linear-gradient(135deg,#6b7a86,#c9c3b8 45%,#3d3f48 80%)}
.eyebrow{font-size:14px;font-weight:600;letter-spacing:.3px}
.about-text{position:absolute;left:643px;top:795px;width:460px}
.about-text h2{font-family:'Cinzel',Georgia,serif;font-weight:400;color:var(--gold);font-size:34px;margin:12px 0 18px}
.about-text p{font-size:13px;line-height:25px;color:var(--muted);margin-bottom:14px}

/* services */
.services{position:absolute;left:0;top:1304px;width:1200px;height:859px;background:radial-gradient(ellipse at 50% 55%,#1e1e1e,#101010 70%)}
.section-title{position:absolute;left:0;width:1200px;text-align:center;font-family:'Cinzel',Georgia,serif;font-weight:400}
.section-sub{position:absolute;left:0;width:1200px;text-align:center;font-size:13.5px;line-height:23px}
.svc-label{position:absolute;font-size:18px;font-weight:600;letter-spacing:.5px}
.svc-desc{position:absolute;width:240px;font-size:10.5px;line-height:19px;color:var(--muted)}

/* reviews */
.review{position:absolute;top:2341px;width:320px;height:293px;border:1.5px solid var(--gold-dark);padding:0 20px}
.avatar{position:absolute;left:18px;top:32px;width:48px;height:48px;border-radius:50%;background:linear-gradient(160deg,#b9c6d2,#5b6a78)}
.stars{position:absolute;left:78px;top:36px;color:var(--gold);font-size:12px;letter-spacing:1px}
.reviewer{position:absolute;left:78px;top:52px;font-size:15px;font-weight:600}
.quote-line{position:absolute;left:18px;right:18px;top:114px;height:1px;background:var(--line)}
.quote-mark{position:absolute;left:52px;top:100px;background:var(--ink);padding:0 6px;color:var(--gold);font-family:Georgia,serif;font-size:30px;line-height:30px;font-weight:700}
.review p{position:absolute;left:20px;right:20px;top:146px;font-size:13.5px;line-height:24.5px}

/* contact band */
.band{position:absolute;left:0;top:2810px;width:1200px;height:310px;background:linear-gradient(100deg,#7d6638 0%,#a98d5b 40%,#b59a68 70%,#8e7646 100%)}

/* blog */
.post{position:absolute;top:3273px;width:317px;height:431px;border:1px solid #55472c;background:var(--ink)}
.post-photo{height:200px}
.post h3{font-family:'Cinzel',Georgia,serif;font-weight:400;font-size:16px;line-height:30px;margin:18px 12px 8px;letter-spacing:.4px}
.post p{font-size:11px;line-height:21px;color:var(--muted);margin:0 12px}

/* contact */
.info h4{font-size:16px;font-weight:700;margin-bottom:8px}
.info p{font-size:14px;line-height:23px}
.social{position:absolute;width:44px;height:44px;border-radius:50%;border:2px solid var(--white);background:var(--gold)}
.form{position:absolute;left:510px;top:3926px;width:530px;height:405px;border:2px solid var(--gold)}
.field{position:absolute;left:36px;right:56px;font-size:14px;color:var(--muted);border-bottom:1px solid var(--line)}
.skyline{position:absolute;left:0;top:4334px;width:1200px;height:290px;background:linear-gradient(180deg,#000 0%,#3b3b3b 35%,#8a8a8a 60%,#4a4a4a 85%,#1a1a1a 100%)}

/* footer */
.footer{position:absolute;left:0;top:4624px;width:1200px;height:427px;background:var(--ink)}
.fcol h5{font-size:15px;font-weight:600;margin-bottom:19px}
.fcol a{display:block;font-size:13.5px;color:var(--white);text-decoration:none;margin-bottom:14.5px}
.fsocial{position:absolute;top:4834px;width:42px;height:42px;border-radius:50%;border:1.5px solid var(--white)}
</style>
</head>
<body>

<!-- HERO -->
<header class="hero">
  <div class="hero-photo" role="img" aria-label="Smiling businessman in glasses and navy blazer seated at a desk with laptop in a dim modern office"></div>
  <div class="hero-shade"></div>
  <div class="brand">Kestwick<br>Holdings AG</div>
  <nav class="nav">
    <a class="active" style="left:420px">Home</a>
    <a style="left:523px">About Us</a>
    <a style="left:647px">Services</a>
    <a style="left:769px">Testimonials</a>
    <a style="left:922px">Blog</a>
    <a style="left:1014px">Contact us</a>
  </nav>
  <h1 class="hero-title" style="font-weight:400">KESTWICK<br>HOLDINGS AG</h1>
  <p class="hero-sub">Sed ut perspiciatis unde omnis iste natus error sit voluptatem accusantium dolore</p>
  <div class="btn-gold" style="left:100px;top:453px;width:157px;height:45px">Get Started</div>
  <svg class="slide-arrow" style="left:58px" width="22" height="46" viewBox="0 0 22 46"><path d="M20 2 L2 23 L20 44" fill="none" stroke="#fff" stroke-width="1.5"/></svg>
  <svg class="slide-arrow" style="left:1116px" width="22" height="46" viewBox="0 0 22 46"><path d="M2 2 L20 23 L2 44" fill="none" stroke="#fff" stroke-width="1.5"/></svg>
</header>
<div class="scroll-dot"><svg width="38" height="38" viewBox="0 0 38 38"><path d="M19 9 V28 M12 21 L19 28 L26 21" fill="none" stroke="#555" stroke-width="2"/></svg></div>

<!-- ABOUT -->
<section>
  <div class="about-frame"></div>
  <div class="about-photo" role="img" aria-label="Three colleagues laughing together around a laptop at an office table"></div>
  <div class="about-text">
    <div class="eyebrow">ABOUT US</div>
    <h2>KESTWICK HOLDINGS AG</h2>
    <p>Sed ut perspiciatis unde omnis iste natus error sit voluptem accusantium doloremque laudantium, totam rem aperiam, eaqa quae ab illo inventore veritatis et quasi architecto beatae vitae dicexplicabo. Nemo enim ipsam voluptatem quia voluptas sit aspernatur aut fugit, sed quia consequuntur magni dolores eos qui ratione voluptatem sequnt.</p>
    <p>Neque porro quisquam est, qui dolorem ipsum quia sit amet consectetur adipiscing elit, sed do eiusmod tempor i labore et dolore magna aliqua. Ut enim ad minim veniam, quis nos</p>
  </div>
  <div class="btn-gold" style="left:643px;top:1133px;width:157px;height:46px">Learn More</div>
</section>

<!-- WHAT WE DO -->
<section class="services">
  <h2 class="section-title" style="top:74px;font-size:52px">WHAT WE DO</h2>
  <p class="section-sub" style="top:150px">Sed ut perspiciatis unde omnis iste natus error sit voluptatem accusantium doloremque laudantium, totam rem<br>aperiam, eaque ipsa quae ab illo inventore veritatis et quasi architecto beatae</p>

  <svg class="abs" style="left:0;top:0" width="1200" height="859" viewBox="0 0 1200 859">
    <defs>
      <linearGradient id="hexGold" x1="0" y1="0" x2="1" y2="1">
        <stop offset="0" stop-color="#e3cc98"/><stop offset=".55" stop-color="#c9ab72"/><stop offset="1" stop-color="#9a7d4a"/>
      </linearGradient>
    </defs>
    <g fill="none" stroke="#fff" stroke-width="2">
      <path d="M245 374 V412 Q245 436 269 436 H453"/>
      <path d="M955 374 V412 Q955 436 931 436 H747"/>
      <path d="M245 570 V532 Q245 508 269 508 H453"/>
      <path d="M955 570 V532 Q955 508 931 508 H747"/>
    </g>
    <g fill="#fff"><circle cx="453" cy="436" r="4"/><circle cx="747" cy="436" r="4"/><circle cx="453" cy="508" r="4"/><circle cx="747" cy="508" r="4"/></g>
    <!-- center hexagon -->
    <polygon points="600,339 718,407 718,545 600,613 482,545 482,407" fill="#1a1a1a" stroke="#c9ab72" stroke-width="2"/>
    <polygon points="600,358 700,416 700,536 600,594 500,536 500,416" fill="url(#hexGold)"/>
    <g fill="#fff"><circle cx="600" cy="339" r="4"/><circle cx="718" cy="407" r="4"/><circle cx="718" cy="545" r="4"/><circle cx="600" cy="613" r="4"/><circle cx="482" cy="545" r="4"/><circle cx="482" cy="407" r="4"/></g>
    <text x="600" y="470" text-anchor="middle" font-family="Cinzel, serif" font-size="22" fill="#fff">KESTWICK</text>
    <text x="600" y="498" text-anchor="middle" font-family="Cinzel, serif" font-size="22" fill="#fff">HOLDINGS</text>
    <!-- small hexagons -->
    <g fill="url(#hexGold)">
      <polygon points="245,245 300,276 300,338 245,369 190,338 190,276"/>
      <polygon points="955,245 1010,276 1010,338 955,369 900,338 900,276"/>
      <polygon points="245,575 300,606 300,668 245,699 190,668 190,606"/>
      <polygon points="955,575 1010,606 1010,668 955,699 900,668 900,606"/>
    </g>
    <g fill="none" stroke="#fff" stroke-width="2" stroke-linecap="round" stroke-linejoin="round">
      <!-- document -->
      <path d="M231 285 H257 L265 293 V330 H231 Z M237 322 V314 M245 322 V306 M253 322 V298"/>
      <!-- advice board -->
      <path d="M935 292 H975 V318 H935 Z M955 318 V330 M942 330 H968 M942 300 H960 M942 308 H968"/>
      <!-- coins -->
      <ellipse cx="236" cy="620" rx="12" ry="4"/><path d="M224 620 V640 Q236 646 248 640 V620"/>
      <circle cx="257" cy="643" r="11"/><path d="M257 637 V649"/>
      <!-- growth chart -->
      <path d="M933 655 V644 M943 655 V637 M953 655 V629 M963 655 V620 M930 655 H980 M934 630 L952 614 L962 620 L978 602 M970 602 H978 V610"/>
    </g>
  </svg>

  <div class="svc-label" style="left:316px;top:262px">FINANCIAL</div>
  <p class="svc-desc" style="left:316px;top:291px">Sed ut perspiciatis unde is iste natus error sit voluptatem accuium doloremque laudantium, totam rem aperiam, eaque</p>
  <div class="svc-label" style="left:640px;top:262px;width:240px;text-align:right">ADVICE</div>
  <p class="svc-desc" style="left:640px;top:291px;text-align:right">Sed ut perspiciatis unde is iste natus error sit voluptatem accuium doloremque laudantium, totam rem aperiam, eaque</p>
  <div class="svc-label" style="left:316px;top:594px">FUNDS</div>
  <p class="svc-desc" style="left:316px;top:623px">Sed ut perspiciatis unde is iste natus error sit voluptatem accuium doloremque laudantium, totam rem aperiam, eaque</p>
  <div class="svc-label" style="left:640px;top:594px;width:240px;text-align:right">GROWTH</div>
  <p class="svc-desc" style="left:640px;top:623px;text-align:right">Sed ut perspiciatis unde is iste natus error sit voluptatem accuium doloremque laudantium, totam rem aperiam, eaque</p>

  <div class="btn-gold" style="left:475px;top:729px;width:250px;height:44px">Interest Rate Calculator</div>
</section>

<!-- REVIEWS -->
<section>
  <h2 class="section-title" style="top:2250px;font-size:40px;color:var(--gold)">CUSTOMER REVIEW</h2>
  <svg class="abs" style="left:1128px;top:2294px" width="34" height="34" viewBox="0 0 34 34"><path d="M30 3 V31 L4 17 Z" fill="none" stroke="#fff" stroke-width="2"/></svg>

  <article class="review" style="left:112px">
    <div class="avatar" role="img" aria-label="Reviewer portrait"></div>
    <div class="stars">★★★★★</div><div class="reviewer">Mara Lindqvist</div>
    <div class="quote-line"></div><div class="quote-mark">”</div>
    <p>Lorem ipsum dolor sit amur adipiscing elit, sed do eiusmod tempor incidit ut labore et dolor ipsum suspendisse ultrices gravida. Risus comm viverra maecenas accumsan lacus vel facilisis.</p>
  </article>
  <article class="review" style="left:453px">
    <div class="avatar" role="img" aria-label="Reviewer portrait"></div>
    <div class="stars">★★★★★</div><div class="reviewer">Mara Lindqvist</div>
    <div class="quote-line"></div><div class="quote-mark">”</div>
    <p>Lorem ipsum dolor sit amur adipiscing elit, sed do eiusmod tempor incidit ut labore et dolor ipsum suspendisse ultrices gravida. Risus comm viverra maecenas accumsan lacus vel facilisis.</p>
  </article>
  <article class="review" style="left:792px">
    <div class="avatar" role="img" aria-label="Reviewer portrait"></div>
    <div class="stars">★★★★★</div><div class="reviewer">Mara Lindqvist</div>
    <div class="quote-line"></div><div class="quote-mark">”</div>
    <p>Lorem ipsum dolor sit amur adipiscing elit, sed do eiusmod tempor incidit ut labore et dolor ipsum suspendisse ultrices gravida. Risus comm viverra maecenas accumsan lacus vel facilisis.</p>
  </article>

  <div class="btn-gold" style="left:520px;top:2669px;width:186px;height:45px">View More</div>
</section>

<!-- CONTACT BAND -->
<section class="band">
  <h2 class="section-title" style="top:64px;font-size:34px">LET'S WORK TOGETHER! CONTACT US</h2>
  <p class="section-sub" style="top:124px;font-size:16px;line-height:30px">Sed ut perspiciatis unde omnis iste natus error sit voluptatem accusantium<br>doloremque laudantium, totam rem aperiam, eaque ipsa</p>
  <div class="btn-outline" style="left:516px;top:198px;width:186px;height:45px;border-color:#fff;color:#fff">Contact Us</div>
</section>

<!-- BLOG -->
<section>
  <h2 class="section-title" style="top:3205px;font-size:40px;color:var(--gold)">LATEST BLOG</h2>
  <article class="post" style="left:102px">
    <div class="post-photo" role="img" aria-label="Colleagues reviewing charts on a laptop at a bright office table" style="background:linear-gradient(135deg,#b9c2c6,#6d7a7d 60%,#3c4446)"></div>
    <h3>The Standard Lorem Ipsum Passage, Used Sihe 1500s</h3>
    <p>Sed ut perspiciatis unde omnis iste natus error sit voluptatem accusantium doloremque laudantium, totam rem aperiam, eaque ipsa</p>
    <div class="btn-outline" style="left:12px;top:369px;width:184px;height:43px">Find Out More ⟶</div>
  </article>
  <article class="post" style="left:441px">
    <div class="post-photo" role="img" aria-label="Business team discussing documents in a modern office" style="background:linear-gradient(135deg,#8a8580,#4a4440 55%,#d6d0c8)"></div>
    <h3>The Standard Lorem Ipsum Passage, Used Sihe 1500s</h3>
    <p>Sed ut perspiciatis unde omnis iste natus error sit voluptatem accusantium doloremque laudantium, totam rem aperiam, eaque ipsa</p>
    <div class="btn-outline" style="left:12px;top:369px;width:184px;height:43px">Find Out More ⟶</div>
  </article>
  <article class="post" style="left:780px">
    <div class="post-photo" role="img" aria-label="Team meeting around laptops in a glass-walled office" style="background:linear-gradient(135deg,#d8dde0,#8c949a 55%,#4d545a)"></div>
    <h3>The Standard Lorem Ipsum Passage, Used Sihe 1500s</h3>
    <p>Sed ut perspiciatis unde omnis iste natus error sit voluptatem accusantium doloremque laudantium, totam rem aperiam, eaque ipsa</p>
    <div class="btn-outline" style="left:12px;top:369px;width:184px;height:43px">Find Out More ⟶</div>
  </article>
</section>

<!-- GET IN TOUCH -->
<section>
  <h2 class="section-title" style="top:3780px;font-size:40px">GET IN TOUCH</h2>
  <p class="section-sub" style="top:3834px;font-size:14px;line-height:26px">At vero eos et accusamus et iustignissimos ducimus qui blanditiis praesentium<br>voluptatum deleniti atque corrupti quos dolores</p>

  <div class="info abs" style="left:159px;top:3952px;width:320px">
    <h4>LOCATION:</h4>
    <p>123 Your Adress Goes Here.<br>CA, 1234567</p>
    <h4 style="margin-top:26px">EMAIL ADDRESS:</h4>
    <p>info@kestwickholdings.example</p>
    <h4 style="margin-top:26px">CALL US NOW:</h4>
    <p>+123 456 7890</p>
    <h4 style="margin-top:26px">FOLLOW NOW:</h4>
  </div>
  <div class="social" style="left:160px;top:4255px" role="img" aria-label="Social profile"></div>
  <div class="social" style="left:213px;top:4255px" role="img" aria-label="Social profile"></div>
  <div class="social" style="left:266px;top:4255px" role="img" aria-label="Social profile"></div>
  <div class="social" style="left:321px;top:4255px" role="img" aria-label="Social profile"></div>

  <form class="form">
    <div class="abs" style="left:36px;top:28px;font-size:16px;font-weight:700">DROP YOUR MESSAGE</div>
    <div class="field" style="top:76px;height:40px">Jonathan Doe
      <svg class="abs" style="right:-36px;top:0" width="18" height="18" viewBox="0 0 18 18"><circle cx="9" cy="6" r="3.5" fill="none" stroke="#ccc"/><path d="M3 17 Q9 9 15 17" fill="none" stroke="#ccc"/></svg></div>
    <div class="field" style="top:150px;height:38px">Email Address
      <svg class="abs" style="right:-36px;top:2px" width="20" height="16" viewBox="0 0 20 16"><rect x="1" y="2" width="18" height="12" fill="none" stroke="#ccc"/><path d="M1 2 L10 9 L19 2" fill="none" stroke="#ccc"/></svg></div>
    <div class="field" style="top:222px;height:72px">Message
      <svg class="abs" style="right:-38px;top:0" width="22" height="20" viewBox="0 0 22 20"><path d="M11 2 Q20 2 20 9 Q20 16 11 16 L5 18 L6 14 Q2 12 2 9 Q2 2 11 2 Z" fill="none" stroke="#ccc"/></svg></div>
    <div class="btn-gold" style="left:251px;top:327px;width:243px;height:45px">Contact Us Now</div>
  </form>
</section>

<div class="skyline" role="img" aria-label="Black and white city skyline with a suspension bridge"></div>

<!-- FOOTER -->
<footer class="footer">
  <div class="abs serif" style="left:100px;top:78px;width:224px;text-align:center;color:var(--gold);font-size:23px;line-height:29px">Kestwick<br>Holdings AG</div>
  <div class="fcol abs" style="left:435px;top:80px">
    <h5>Quick Link</h5><a>Home</a><a>About Us</a><a>Our Platform</a><a>Our Team</a><a>Blog</a><a>Contact us</a>
  </div>
  <div class="fcol abs" style="left:668px;top:80px">
    <h5>Other Link</h5><a>Who We Are</a><a>Career</a><a>News</a><a>Resources</a><a>Contact</a>
  </div>
  <div class="fcol abs" style="left:851px;top:80px;width:250px">
    <h5>Contact Info</h5>
    <div style="display:flex;gap:8px;font-size:13.5px;line-height:19px"><svg width="12" height="16" viewBox="0 0 12 16"><path d="M6 15 Q0 8 1 5 A5 5 0 0 1 11 5 Q12 8 6 15 Z" fill="#c9ab72"/><circle cx="6" cy="5.5" r="2" fill="#0b0b0b"/></svg><span>123 Your Adress Goes Here.<br>CA, 1234567</span></div>
    <div style="display:flex;gap:8px;font-size:13.5px;margin-top:13px"><svg width="14" height="14" viewBox="0 0 14 14"><path d="M2 1 L5 1 L6 4 L4 5.5 Q6 8.5 8.5 10 L10 8 L13 9 L13 12 Q12 13 10 13 Q2 11 1 3 Q1 1 2 1 Z" fill="#c9ab72"/></svg><span>+123 456 7890</span></div>
    <div style="display:flex;gap:8px;font-size:13.5px;margin-top:13px"><svg width="14" height="12" viewBox="0 0 14 12"><rect x="0" y="1" width="14" height="10" fill="#c9ab72"/><path d="M0 1 L7 7 L14 1" fill="none" stroke="#0b0b0b"/></svg><span>info@kestwickholdings.example</span></div>
  </div>
  <div class="fsocial" style="left:105px;top:210px" role="img" aria-label="Social profile"></div>
  <div class="fsocial" style="left:159px;top:210px" role="img" aria-label="Social profile"></div>
  <div class="fsocial" style="left:212px;top:210px" role="img" aria-label="Social profile"></div>
  <div class="fsocial" style="left:267px;top:210px" role="img" aria-label="Social profile"></div>
  <div class="abs" style="left:100px;top:378px;font-size:13px">Copyright © 2022 - Kestwick Holdings AG. All Right Reserved</div>
  <div class="abs" style="right:102px;top:378px;font-size:13px">Privacy Policy &nbsp;|&nbsp; Terms &amp; Conditions</div>
</footer>

</body>
</html>
```